Velmori Martial Art - Online Training

We currently have a website that we love the look and feel of at http://test.velmori.com.au/ which we are about to launch. This site is focused on face to face training we provide in private and group lessons around Australia.

We have another site we will be launching for Velmori and this one is for their online training system that will be available wordwide. The difference with this site is that it is promoting and providing access to an online training course whereas the other Velmori site you did the design for was for the face to face training they do.

The new site can be viewed at https://www.velmorimartialart.com/default.aspx (it's not live yet)

Can you please come up with a design with a similar feel to http://test.velmori.com.au/ but it also needs to be clear that it's for the online course so that people don't get confused between the two sites.

```html
<!DOCTYPE html>
<html lang="en">
<head>
<meta charset="utf-8">
<title>Velmori Martial Art – Online Training</title>
<link rel="stylesheet" href="https://fonts.googleapis.com/css2?family=Poppins:wght@400;600;700&display=swap">
<style>
:root{
  --gold:#d3ab35;
  --ink:#191c21;
  --white:#ffffff;
  --photo-dark:#2b3a2e;
  --photo-light:#6f8a4f;
}
*{box-sizing:border-box;margin:0;padding:0}
html,body{width:1200px;height:4083px;overflow:hidden}
body{background:var(--ink);font-family:"Poppins",sans-serif;color:var(--white);position:relative}
.abs{position:absolute}
.promo-bar{left:0;top:0;width:1200px;height:106px;background:var(--gold)}
.promo-text{left:127px;top:40px;font-weight:700;font-size:16px}
.promo-btn{left:915px;top:38px;width:163px;height:32px;background:var(--ink);border-radius:4px;font-size:14px;display:flex;align-items:center;justify-content:center}
.hero-photo{left:0;top:106px;width:1200px;height:488px;background:linear-gradient(180deg,var(--photo-dark),var(--photo-light) 70%,#4d6a37)}
.welcome-box{left:108px;top:525px;width:984px;height:138px;background:var(--gold);display:flex;align-items:center;justify-content:center;text-align:center;font-weight:700;font-size:31px;line-height:45px}
.intro{left:122px;top:716px;width:961px;font-size:15px;line-height:29px}
.intro p{margin-bottom:29px}
.start-btn{left:518px;top:1317px;width:164px;height:32px;background:var(--gold);border-radius:6px;font-size:14px;display:flex;align-items:center;justify-content:center}
.divider{left:0;top:1398px;width:1200px;height:8px;background:var(--gold)}
.master-box{left:108px;top:1506px;width:816px;height:1222px;background:var(--gold)}
.master-title{left:158px;top:1555px;font-weight:700;font-size:42px}
.master-bio{left:158px;top:1640px;font-size:15px;line-height:29px}
.master-bio p{margin-bottom:29px}
.master-bio .narrow{width:480px}
.master-bio .wide{width:720px}
.master-photo{left:691px;top:1557px;width:400px;height:597px;background:linear-gradient(180deg,#000 0%,#1a1a1f 60%,#1d2436 100%)}
.testimonials-title{left:0;top:2825px;width:1200px;text-align:center;color:var(--gold);font-weight:700;font-size:42px}
.quote-mark{left:570px;width:60px;height:40px}
.quote-text{left:118px;width:964px;text-align:center;font-size:15px;line-height:29px}
.quote-text p{margin-bottom:29px}
.avatar{width:110px;height:110px;border-radius:50%;background:radial-gradient(circle at 50% 40%,#9aa3ad,#3c4a5a)}
.author{left:0;width:1200px;text-align:center;font-weight:700;font-size:15px;line-height:29px}
</style>
</head>
<body>
<div class="abs promo-bar"></div>
<div class="abs promo-text">5% of our proceeds from the online course are donated to a different charity each month!</div>
<div class="abs promo-btn">Read More</div>

<div class="abs hero-photo" role="img" aria-label="Outdoor group training photo of students sparring with sticks on a grass field"></div>
<div class="abs welcome-box">Welcome to Velmori Martial Art. We are excited to share<br>this amazing art with you.</div>

<div class="abs intro">
<p>Velmori Martial Art was created for the real world. It is not, nor has it ever been, a ‘ring’ or competition based style of sport. With deep roots in the traditional Burmese martial art ‘Burmese Thaing’, Master Daniel Maren adapted this traditional art to create an effective, highly adaptable and no-nonsense self-protection style that suits our modern world.</p>
<p>Velmori Martial Art teaches you how to use your whole body as a weapon - from elbows to knees, open palms, edge hands, closed fists, locks, deflections, traps, blocks, bridges, kicks, forearms, your head – the list goes on! With consistent training you will develop impenetrable defences and intricate footwork that allow you to dynamically flow around an opponent, giving you a huge advantage in a street situation.</p>
<p>You will learn to move your body in dynamic ways by developing a greater understanding of body weight, momentum and how to move with a path of least resistance. You will develop an advanced understanding of energy slings and circuits to produce movements with precision, speed, power and flow. You will learn how to use your opponent’s size and energy against them, meaning you don’t have to be the biggest person in the room to protect yourself effectively.</p>
<p>We believe everyone has the right to feel safe and have the ability to protect themselves and their loved ones. There is no limit to how dynamic and adaptable you can become on your Velmori journey. Velmori provides you with many choices for how you can respond in any situation, with our main focus always being the personal safety and wellbeing of both you and your loved ones.</p>
<p>We are excited for your journey towards greater levels of empowerment.</p>
</div>
<div class="abs start-btn">Start Journey</div>
<div class="abs divider"></div>

<div class="abs master-box"></div>
<div class="abs master-title">Master Daniel Maren</div>
<div class="abs master-photo" role="img" aria-label="Portrait of the chief instructor in a dark training shirt"></div>
<div class="abs master-bio">
<p class="narrow">Daniel (Ne Varun) Maren was born in Myanmar (formerly known as Burma) and was taught a form of Thaing by a close family member from a young age.</p>
<p class="narrow">In 1993, at the age of 22, Daniel started teaching his closest friends his form of Thaing and so Velmori Martial Art was born.</p>
<p class="narrow">At that time, Daniel had graduated with a Bachelor of Commerce Degree and was offered several career opportunities but a corporate career was never Daniel’s dream, so he continued to spend his time teaching martial arts to his closest friends and working several part-time jobs.</p>
<p class="narrow" style="margin-bottom:15px">His passion and dedication to Velmori Martial Art was infectious and he began to attract more and more students. Daniel has now been training martial arts for over 40 years and teaching Velmori since 1993. Daniel has adapted his traditional art to suit our modern lifestyle and requirements</p>
<p class="wide">Daniel has spent almost 30 years as a Personal Coach, and a Martial Arts Instructor. He has personally taught and coached tens of thousands of people and spent over 50,000 hours teaching. Daniel has had the pleasure and the privilege of coaching people from all walks of life, ranging from super successful businessman, world class athletes, home makers, policewomen, people in the military, Doctors, teachers, lawyers and much more. These people have aged from 80 years old to 3 years old.</p>
<p class="wide">Daniel is a dedicated husband and father. When Daniel is not training Velmori, you will find him teaching Velmori to the next generation, his sons, or spending time with his family, mountain biking, snowboarding, at the beach, training at the gym, reading and meditating. Spiritual growth and self- awareness are high on Daniel’s hierarchy of values.</p>
<p class="wide">Daniel considers teaching a true privilege; he believes that his calling in life is to be of service to people through sharing Velmori Martial Art.</p>
<p class="wide">You now have the unique opportunity to train Velmori Martial Art and learn directly from the Master from anywhere in the world.</p>
</div>

<div class="abs testimonials-title">Testimonials</div>

<svg class="abs quote-mark" style="top:2948px" viewBox="0 0 60 40" aria-hidden="true"><path fill="#fff" d="M4 36c0-16 6-28 18-32l2 4c-7 4-9 9-9 13 5 0 9 4 9 8s-4 7-10 7S4 40 4 36zM32 36c0-16 6-28 18-32l2 4c-7 4-9 9-9 13 5 0 9 4 9 8s-4 7-10 7-10-4-10-8z"/></svg>
<div class="abs quote-text" style="top:3026px">
<p>We all need a mentor in our life that knows how to get the best out of you, and I'm extremely grateful that Chief Instructor Daniel Maren is my mentor, I don't know where I would be if I didn't have his guidance. Daniel has added so much value to my life and my family's life.</p>
<p>As a Martial Artist Daniel is one of a kind, I've been getting coached by him for the last 17 years and every time he moves, it blows my mind and inspires me to be the Martial Artist I can be.</p>
</div>
<div class="abs avatar" style="left:545px;top:3240px" role="img" aria-label="Portrait of senior instructor"></div>
<div class="abs author" style="top:3376px">Velmori Martial Art<br>3rd Degree Senior Instructor<br>Liam Treloar</div>

<svg class="abs quote-mark" style="top:3527px" viewBox="0 0 60 40" aria-hidden="true"><path fill="#fff" d="M4 36c0-16 6-28 18-32l2 4c-7 4-9 9-9 13 5 0 9 4 9 8s-4 7-10 7S4 40 4 36zM32 36c0-16 6-28 18-32l2 4c-7 4-9 9-9 13 5 0 9 4 9 8s-4 7-10 7-10-4-10-8z"/></svg>
<div class="abs quote-text" style="top:3605px">
<p>I’ve been training in various martial arts for over 20 years, across boxing, BJJ, hapkido and krav maga, collecting a black belt in hapkido along the way. I’ve been lucky enough to train with some amazing martial artists and under some incredible instructors. Chief Instructor Daniel Maren stands out even amongst this group. As a martial artist, he personifies what first attracted me to Velmori Martial Art – fast, fluid, powerful application of practical techniques. As an instructor, he has an amazing (and amazingly helpful!) knack for not just teaching rote technique, but for helping you understand how to best train and apply those techniques for your body. And finally as a person, probably the best testament to Chief Instructor Daniel Maren is what he has accomplished with Velmori Martial Art in Australia. He’s built a passionate community of martial artists who train hard and push each other, but always with the utmost respect. Who give back to the community both directly and through a range of charities, and are always open, warm and welcoming to new members.</p>
</div>
<div class="abs avatar" style="left:545px;top:3889px" role="img" aria-label="Portrait of student"></div>
<div class="abs author" style="top:4025px">Marco Villeni</div>
</body>
</html>
```